Harbinger Slabworks, Inc. Business Card

Create a business card that is eye catching and based around concrete sawcutting. I've attached our current business card and logo for reference. We like aspects of the current business card, but it is starting to feel very loud and lost. We would like something that is still fun but is more modern and streamlined.

```html
<!DOCTYPE html>
<html lang="en">
<head>
<meta charset="utf-8">
<title>Harbinger Slabworks, Inc. Business Card</title>
<link href="https://fonts.googleapis.com/css2?family=Tinos:wght@400;700&family=Open+Sans:wght@400;600&display=swap" rel="stylesheet">
<style>
  :root {
    --page: #3a3b3d;
    --card: #ffffff;
    --card-shade: #ececec;
    --red: #c8202a;
    --navy: #1f2a6b;
    --gold: #e6b822;
    --ink: #2b2b2b;
    --watermark-a: #e9e6dc;
    --watermark-b: #f4f4f4;
  }
  * { box-sizing: border-box; margin: 0; padding: 0; }
  html, body { width: 1200px; height: 900px; overflow: hidden; }
  body { background: var(--page); font-family: "Tinos", "Times New Roman", serif; color: var(--ink); position: relative; }

  .card {
    position: absolute; width: 640px; height: 366px;
    background: linear-gradient(160deg, var(--card) 0%, var(--card-shade) 55%, var(--card) 100%);
    box-shadow: 0 14px 30px rgba(0,0,0,.45);
    overflow: hidden;
  }
  .card--front { left: 60px; top: 60px; }
  .card--back { left: 500px; top: 474px; }

  .watermark {
    position: absolute; border-radius: 50% 40% 45% 55%;
    background: radial-gradient(ellipse at 35% 50%, var(--watermark-a) 0%, var(--watermark-b) 70%, transparent 100%);
    opacity: .8;
  }
  .card--front .watermark { left: 300px; top: 20px; width: 300px; height: 230px; }
  .card--back .watermark { left: 40px; top: 120px; width: 300px; height: 200px; }

  .brand { position: absolute; display: flex; align-items: center; gap: 10px; }
  .brand__dot { width: 26px; height: 26px; border-radius: 50%; background: var(--navy); flex: none; }
  .brand__name { font-size: 20px; font-weight: 700; color: var(--navy); line-height: 1.1; width: 150px; }
  .card--front .brand { left: 40px; top: 50px; }
  .card--back .brand { right: 40px; top: 44px; }

  .heading-row { display: flex; align-items: center; gap: 20px; }
  .rule { flex: 1; height: 1px; }
  .card--front .rule { background: var(--red); }
  .card--back .rule { background: var(--navy); }

  .services { position: absolute; left: 40px; right: 50px; top: 150px; }
  .services__title { font-size: 22px; font-weight: 700; color: var(--red); letter-spacing: .5px; white-space: nowrap; }
  .services__list { list-style: none; font-size: 17px; line-height: 1.6; margin-top: 8px; }
  .services__list li { display: flex; align-items: center; gap: 8px; padding-left: 8px; }
  .star { width: 13px; height: 13px; fill: var(--gold); flex: none; }

  .hotline { position: absolute; right: 40px; top: 200px; display: flex; align-items: center; gap: 8px;
    font-family: "Open Sans", Arial, sans-serif; font-size: 24px; color: var(--red); }
  .icon { width: 16px; height: 16px; fill: var(--red); flex: none; }
  .hotline .icon { width: 20px; height: 20px; }

  .person { position: absolute; left: 40px; right: 30px; top: 158px; }
  .person__name { font-size: 24px; font-weight: 700; color: var(--red); letter-spacing: .5px; white-space: nowrap; }
  .person__role { font-size: 18px; color: var(--navy); margin-top: 2px; }
  .contact { list-style: none; margin-top: 14px; font-size: 16px; line-height: 1.55; }
  .contact li { display: flex; align-items: center; gap: 10px; }
</style>
</head>
<body>

<section class="card card--front" aria-label="Business card front">
  <div class="watermark" role="img" aria-label="Faint eagle head illustration"></div>
  <div class="brand"><span class="brand__dot"></span><span class="brand__name">Harbinger Slabworks, Inc.</span></div>
  <div class="services">
    <div class="heading-row">
      <h2 class="services__title">OUR SERVICES</h2>
      <span class="rule"></span>
    </div>
    <ul class="services__list">
      <li><svg class="star" viewBox="0 0 24 24"><polygon points="12,1 15,9 23,9 17,14 19,23 12,18 5,23 7,14 1,9 9,9"/></svg>Wall Sawing</li>
      <li><svg class="star" viewBox="0 0 24 24"><polygon points="12,1 15,9 23,9 17,14 19,23 12,18 5,23 7,14 1,9 9,9"/></svg>Core Drilling</li>
      <li><svg class="star" viewBox="0 0 24 24"><polygon points="12,1 15,9 23,9 17,14 19,23 12,18 5,23 7,14 1,9 9,9"/></svg>Slab Sawing</li>
      <li><svg class="star" viewBox="0 0 24 24"><polygon points="12,1 15,9 23,9 17,14 19,23 12,18 5,23 7,14 1,9 9,9"/></svg>Breaking &amp; Removal</li>
    </ul>
  </div>
  <div class="hotline">
    <svg class="icon" viewBox="0 0 24 24"><path d="M6.6 10.8a15 15 0 0 0 6.6 6.6l2.2-2.2c.3-.3.7-.4 1-.2 1.1.4 2.3.6 3.6.6.6 0 1 .4 1 1V20c0 .6-.4 1-1 1A17 17 0 0 1 3 4c0-.6.4-1 1-1h3.5c.6 0 1 .4 1 1 0 1.3.2 2.5.6 3.6.1.3 0 .7-.2 1z"/></svg>
    555-Slabcut
  </div>
</section>

<section class="card card--back" aria-label="Business card back">
  <div class="watermark" role="img" aria-label="Faint eagle head illustration"></div>
  <div class="brand"><span class="brand__dot"></span><span class="brand__name">Harbinger Slabworks, Inc.</span></div>
  <div class="person">
    <div class="heading-row">
      <h1 class="person__name">MARISSA DELANO</h1>
      <span class="rule"></span>
    </div>
    <p class="person__role">Operations and Finance</p>
    <ul class="contact">
      <li><svg class="icon" viewBox="0 0 24 24"><path d="M7 1h10a2 2 0 0 1 2 2v18a2 2 0 0 1-2 2H7a2 2 0 0 1-2-2V3a2 2 0 0 1 2-2zm0 3v14h10V4z"/></svg>555.014.2231</li>
      <li><svg class="icon" viewBox="0 0 24 24"><path d="M6.6 10.8a15 15 0 0 0 6.6 6.6l2.2-2.2c.3-.3.7-.4 1-.2 1.1.4 2.3.6 3.6.6.6 0 1 .4 1 1V20c0 .6-.4 1-1 1A17 17 0 0 1 3 4c0-.6.4-1 1-1h3.5c.6 0 1 .4 1 1 0 1.3.2 2.5.6 3.6.1.3 0 .7-.2 1z"/></svg>555.018.4470</li>
      <li><svg class="icon" viewBox="0 0 24 24"><path d="M2 5h20v14H2zm2 2v.4l8 5 8-5V7z"/></svg>marissa@harbingerslabworks.com</li>
      <li><svg class="icon" viewBox="0 0 24 24"><path d="M12 2a10 10 0 1 0 0 20 10 10 0 0 0 0-20zm0 2c1 1.3 1.8 3 2.1 5H9.9C10.2 7 11 5.3 12 4zM4.3 11h3.6a16 16 0 0 0 0 2H4.3a8 8 0 0 1 0-2zm5.6 0h4.2a14 14 0 0 1 0 2H9.9a14 14 0 0 1 0-2zm6.2 0h3.6a8 8 0 0 1 0 2h-3.6a16 16 0 0 0 0-2zM9.9 15h4.2c-.3 2-1.1 3.7-2.1 5-1-1.3-1.8-3-2.1-5z"/></svg>www.harbingerslabworks.com</li>
      <li><svg class="icon" viewBox="0 0 24 24"><path d="M12 1a7 7 0 0 0-7 7c0 5 7 15 7 15s7-10 7-15a7 7 0 0 0-7-7zm0 10a3 3 0 1 1 0-6 3 3 0 0 1 0 6z"/></svg>48 Quarry Hill Road, Fairbrook, NJ 07000</li>
    </ul>
  </div>
</section>

</body>
</html>
```